Redesign Canvas Art E-Commerce Website

Help! I hired a couple of companies on Tasklyn.com to build and design an e-commerce website for me. After three long and painful months, I have one that I believe is functional on the back-end, but aesthetically on the front end is a mess.

We are a small family business that will take your digital photo and manipulate it into a digitally created oil, watercolor or impressionist style pieces of artwork that we print on museum quality, gallery grade canvas and ship to the customer, ready to hang.

We are looking to create an e-commerce website where a customer can choose their art style, upload a photo, choose their canvas size and orientation (horizontal or vertical) and checkout. Within 48 hours, we will send them back a proof of their newly created, customized artwork for them to approve or not approve. If they approve, we print, package and ship them the product. If they do not approve, we offer unlimited revisions until they are happy.

As I mentioned, the back end functionality is already there, just need design help. No coding required

Here is a link to the development page that they created: https://brushvellomart.com/development/

As you can see, it looks off...doesnt line up properly, wasted space, weird font. Feel free to either correct the homepage they created or design an entirely new page. I am attaching some examples of before and after photos of artwork for reference. I also think the testimonials page and shop page can use a little style. The content is there and accurate, it just doesn't look pretty. Please keep in mind that our customers will probably not be very tech savvy. The customers will probably be sending us pics of kids, grandkids, pets, family portraits, vacation photos, etc.

Here is one of our competitors - www.pelfandquill.com
Their website looks clean and inviting.

Thank you in advance! Im looking forward to seeing the results. I am including our logo in the attachments (I do not have it in a vector file, just a jpeg)

Target Market(s)

Non tech-savvy indiduals, 30-70 years old

Industry/Entity Type

Please look at https://brushvellomart.com/development/ to see various pages and what the other designers did

Number of Pages Required

1 page

Requirements
Must have
• Verbiage on pages leave "as is" but feel free to change styles. Would like to keep existing four categories on homepage
Nice to have
• Warm and inviting homepage that evokes emotion

```html
<!DOCTYPE html>
<html lang="en">
<head>
<meta charset="utf-8">
<title>Brushvello Art – Turn Your Digital Photos Into Wall Art</title>
<link rel="stylesheet" href="https://fonts.googleapis.com/css2?family=Mulish:wght@400;600;700;800;900&display=swap">
<style>
:root{
  --orange:#ef5a24;
  --ink:#1a1a1a;
  --text:#444;
  --band:#f5f3f3;
  --circle:#f1efef;
  --white:#fff;
  --black:#000;
}
*{margin:0;padding:0;box-sizing:border-box}
html,body{width:1200px;height:4270px;overflow:hidden}
body{position:relative;background:var(--white);font-family:"Mulish",Arial,sans-serif;color:var(--ink)}
.abs{position:absolute}
.topbar{left:0;top:0;width:1200px;height:33px;background:var(--black);color:var(--white);font-size:13px;font-weight:600;text-align:center;line-height:33px;letter-spacing:.3px}
.logo{display:flex;align-items:center;gap:10px;color:var(--ink);font-weight:800;font-size:26px;white-space:nowrap}
.logo .dot{width:30px;height:30px;border-radius:50%;background:var(--orange)}
.site-logo{left:133px;top:62px}
.nav{top:70px;left:410px;font-size:14.5px}
.nav a{color:var(--ink);text-decoration:none;position:absolute;white-space:nowrap}
.nav a.active{color:var(--orange);border-bottom:1px solid var(--orange)}
.cart{left:1030px;top:62px}
.hero{left:133px;top:132px;width:936px;height:534px;background:radial-gradient(ellipse at 58% 42%,#d8c3ad 0%,#8a6f4c 22%,#3f5a2a 50%,#26401c 80%,#1c3015 100%)}
.hero h1{position:absolute;left:59px;top:82px;color:var(--white);font-size:41px;font-weight:900;line-height:44px;white-space:nowrap}
.btn{display:inline-block;background:var(--orange);color:var(--white);font-weight:800;font-size:13px;text-align:center;text-decoration:none;letter-spacing:.3px}
.hero .btn{position:absolute;left:63px;top:287px;width:172px;height:47px;line-height:47px}
.dots{position:absolute;left:433px;top:495px;display:flex;gap:9px}
.dots span{width:9px;height:9px;border-radius:50%;background:var(--white)}
.dots span.on{background:var(--orange)}
.section-title{left:0;width:1200px;text-align:center;font-size:24px;font-weight:800;text-transform:uppercase}
.section-title::after{content:"";display:block;width:35px;height:3px;background:var(--orange);margin:16px auto 0}
.cat-img{width:446px;height:313px}
.cat-label{font-size:19px;font-weight:700;width:298px;padding-bottom:12px;border-bottom:1px dotted #888}
.cat-btn{width:131px;height:35px;line-height:35px}
.step{width:240px;text-align:center}
.badge{width:112px;height:112px;margin:0 auto;border-radius:50%;background:var(--circle);display:flex;align-items:center;justify-content:center}
.step-num{display:inline-block;margin-top:56px;padding:3px 10px;border:1px solid #e2e2e2;font-size:14px;color:var(--text)}
.step-title{margin-top:18px;font-size:16px;font-weight:600;white-space:nowrap}
.about{left:0;top:2033px;width:1200px;height:469px;background:var(--band)}
.about-img{left:133px;top:57px;width:435px;height:354px;background:linear-gradient(135deg,#9fb67a,#d9d4c2 50%,#8eb0c4)}
.about-copy{left:620px;top:53px;width:440px}
.about-copy h2{font-size:24px;font-weight:800}
.about-copy h2::after{content:"";display:block;width:35px;height:3px;background:var(--orange);margin-top:12px}
.about-copy p{font-size:13.5px;line-height:22px;color:var(--text);margin-top:20px}
.about-copy p+p{margin-top:14px}
.about-copy .btn{margin-top:28px;width:132px;height:36px;line-height:36px}
.creation{top:2630px;width:300px;height:315px}
.arrow{color:#999;font-size:40px;font-weight:300}
.testimonials{left:0;top:3054px;width:1200px;height:525px;background:var(--band)}
.t-card{top:127px;width:298px;height:345px;background:var(--white);border:1px solid #e2e2e2;text-align:center;padding:28px 34px 0}
.t-card .q{color:var(--orange);font-size:46px;font-weight:900;line-height:40px;font-family:Georgia,serif}
.t-card .stars{color:var(--orange);font-size:13px;letter-spacing:2px;margin-top:4px}
.t-card p{font-size:12.5px;line-height:19px;color:var(--text);margin-top:14px}
.t-card .sep{width:26px;height:1px;background:var(--orange);margin:20px auto}
.t-card .name{font-weight:800;font-size:13.5px}
.t-card .place{font-size:12.5px;color:var(--text);margin-top:3px}
.why{width:240px;text-align:center}
.why h3{margin-top:58px;font-size:17px;font-weight:700}
.why p{margin-top:14px;font-size:12.5px;line-height:19px;color:var(--text)}
.footer{left:0;top:4048px;width:1200px;height:222px;background:var(--black);color:var(--white)}
.footer .logo{color:var(--white)}
.foot-contact{left:665px;top:30px;display:flex;gap:14px;font-size:13.5px;line-height:20px}
.follow{left:945px;top:26px;font-size:13.5px}
.socials{left:943px;top:52px;display:flex;gap:9px}
.socials span{width:26px;height:26px;border-radius:50%;border:1.5px solid #bbb}
.foot-links{left:380px;top:96px;font-size:12.5px;white-space:nowrap;color:#ddd}
.foot-links span{margin:0 10px;color:#aaa}
.foot-rule{left:380px;top:139px;width:688px;height:1px;background:#333}
.copyright{left:0;top:174px;width:1200px;text-align:center;font-size:11.5px;color:#ddd}
</style>
</head>
<body>

<div class="abs topbar">FREE SHIPPING FOR ALL USA &nbsp;ORDERS</div>

<header>
  <div class="abs logo site-logo"><span class="dot"></span>Brushvello Art</div>
  <nav class="abs nav">
    <a class="active" style="left:0">Home</a>
    <a style="left:75px">Shop</a>
    <a style="left:140px">Testimonials</a>
    <a style="left:255px">About Us</a>
    <a style="left:349px">FAQs</a>
    <a style="left:420px">My Orders</a>
    <a style="left:524px">Contact Us</a>
  </nav>
  <svg class="abs cart" width="38" height="32" viewBox="0 0 38 32" aria-label="Cart">
    <path d="M2 5h5l4 16h16l4-11H10" fill="none" stroke="#1a1a1a" stroke-width="2"/>
    <circle cx="13" cy="26" r="2.2" fill="#1a1a1a"/><circle cx="25" cy="26" r="2.2" fill="#1a1a1a"/>
    <circle cx="32" cy="7" r="7" fill="#ef5a24"/><text x="32" y="10" font-size="9" fill="#fff" text-anchor="middle" font-family="Mulish,sans-serif">0</text>
  </svg>
</header>

<section class="abs hero" role="img" aria-label="Painted portrait of a bride and groom embracing in front of ivy">
  <h1>Turn Your Digital<br>Photos Into<br>One of a Kind<br>Wall Art</h1>
  <a class="btn">GET STARTED</a>
  <div class="dots"><span></span><span class="on"></span><span></span><span></span></div>
</section>

<h2 class="abs section-title" style="top:707px">Categories</h2>

<div class="abs cat-img" style="left:133px;top:792px;background:linear-gradient(135deg,#e6e0da,#c98a48 35%,#8a5a32 70%,#d9d4cf)" role="img" aria-label="Oil painting of a dog and cat resting together"></div>
<div class="abs cat-label" style="left:131px;top:1124px">Oil</div>
<a class="abs btn cat-btn" style="left:446px;top:1127px">GET STARTED</a>

<div class="abs cat-img" style="left:620px;top:792px;background:linear-gradient(135deg,#f3ece8,#e6cfc2 45%,#f7f1ee)" role="img" aria-label="Watercolor of a mother with her baby"></div>
<div class="abs cat-label" style="left:620px;top:1124px">Watercolor</div>
<a class="abs btn cat-btn" style="left:935px;top:1127px">GET STARTED</a>

<div class="abs cat-img" style="left:133px;top:1198px;background:linear-gradient(180deg,#8db8dc,#3c8fb0 35%,#2fb59a 60%,#c4a888)" role="img" aria-label="Impressionist painting of a woman by a canal with gondolas"></div>
<div class="abs cat-label" style="left:129px;top:1530px">Impressionist</div>
<a class="abs btn cat-btn" style="left:446px;top:1532px">GET STARTED</a>

<div class="abs cat-img" style="left:620px;top:1198px;background:linear-gradient(160deg,#34501f,#7f8a5c 45%,#b5aa94)" role="img" aria-label="Photo of a father and child walking on a forest path"></div>
<div class="abs cat-label" style="left:620px;top:1530px">Digital Photo</div>
<a class="abs btn cat-btn" style="left:935px;top:1532px">GET STARTED</a>

<h2 class="abs section-title" style="top:1634px">Our Process</h2>

<div class="abs step" style="left:92px;top:1750px">
  <div class="badge"><svg width="48" height="48" viewBox="0 0 48 48" fill="none" stroke="#ef5a24" stroke-width="2.2"><rect x="6" y="8" width="34" height="32" rx="8"/><path d="M8 34l10-10 8 8 5-5 9 9"/><circle cx="16" cy="18" r="3"/><path d="M34 4v12M29 9l5-5 5 5"/></svg></div>
  <span class="step-num">Step 1</span>
  <div class="step-title">Upload your photo</div>
</div>
<div class="abs step" style="left:331px;top:1750px">
  <div class="badge"><svg width="48" height="48" viewBox="0 0 48 48" fill="none" stroke="#ef5a24" stroke-width="2.2"><rect x="7" y="5" width="34" height="38"/><rect x="12" y="10" width="24" height="28"/><path d="M12 30l8-8 6 6 4-4 6 6"/></svg></div>
  <span class="step-num">Step 2</span>
  <div class="step-title">Choose your style</div>
</div>
<div class="abs step" style="left:588px;top:1750px">
  <div class="badge"><svg width="48" height="48" viewBox="0 0 48 48" fill="none" stroke="#ef5a24" stroke-width="2.2"><rect x="6" y="22" width="20" height="20"/><rect x="18" y="6" width="24" height="24"/><path d="M24 24l12-12M28 12h8v8"/></svg></div>
  <span class="step-num">Step 3</span>
  <div class="step-title">Choose your size</div>
</div>
<div class="abs step" style="left:855px;top:1750px">
  <div class="badge"><svg width="48" height="48" viewBox="0 0 48 48" fill="none" stroke="#ef5a24" stroke-width="2.2"><rect x="8" y="12" width="32" height="28"/><rect x="13" y="17" width="22" height="18"/><path d="M18 12l6-6 6 6"/></svg></div>
  <span class="step-num">Step 4</span>
  <div class="step-title">Choose your orientation</div>
</div>

<section class="abs about">
  <div class="abs about-img" role="img" aria-label="Painted portrait of a laughing older couple outdoors"></div>
  <div class="abs about-copy">
    <h2>ABOUT US</h2>
    <p>At Brushvello Art, we take your digital photo and turn it<br>into a one-of-a-kind piece of artwork!</p>
    <p>The process couldn’t be any easier. Simply upload your photo, choose your art style and size, and let our team of skilled digital artists do the rest. Do you want to put your digital photo on canvas without an art style? No problem! Just choose the “Digital Photo/Retouching” category and upload your photo. We can print your photo “as is” or do some minor retouching (e.g. remove objects, enhance colors, lighten photo, etc)</p>
    <a class="btn">READ MORE</a>
  </div>
</section>

<h2 class="abs section-title" style="top:2552px">Recent Creations</h2>
<div class="abs arrow" style="left:64px;top:2752px">&#8249;</div>
<div class="abs creation" style="left:131px;background:linear-gradient(135deg,#2e4a22,#5c6a3a 45%,#9a9590)" role="img" aria-label="Finished bride and groom canvas shown beside the original phone photo"></div>
<div class="abs creation" style="left:451px;background:linear-gradient(160deg,#4a6a32,#a9a288 50%,#dcbfa4)" role="img" aria-label="Father and child canvas with the source photo on a phone"></div>
<div class="abs creation" style="left:769px;background:linear-gradient(135deg,#6a4324,#d08a44 50%,#ece7e1)" role="img" aria-label="Dog and cat canvas with the source photo on a phone"></div>
<div class="abs arrow" style="left:1102px;top:2752px">&#8250;</div>
<a class="abs btn" style="left:548px;top:2971px;width:103px;height:36px;line-height:36px">VIEW ALL</a>

<section class="abs testimonials">
  <h2 class="abs section-title" style="top:50px">Testimonials</h2>
  <div class="abs arrow" style="left:64px;top:300px">&#8249;</div>
  <div class="abs arrow" style="left:1102px;top:300px">&#8250;</div>
  <div class="abs t-card" style="left:133px"><div class="q">&ldquo;</div><div class="stars">★★★★★</div><p>My mom is in an assisted living facility and has Alzheimers. We had a family portrait made into an oil and put in her room to help her remember us. The nurses always tell us how much she loves it and helps jog her memory. Thank you Brushvello Art!</p><div class="sep"></div><div class="name">Helen R</div><div class="place">Potomac, MD</div></div>
  <div class="abs t-card" style="left:451px"><div class="q">&ldquo;</div><div class="stars">★★★★★</div><p>My mom is in an assisted living facility and has Alzheimers. We had a family portrait made into an oil and put in her room to help her remember us. The nurses always tell us how much she loves it and helps jog her memory. Thank you Brushvello Art!</p><div class="sep"></div><div class="name">Helen R</div><div class="place">Potomac, MD</div></div>
  <div class="abs t-card" style="left:769px"><div class="q">&ldquo;</div><div class="stars">★★★★★</div><p>My mom is in an assisted living facility and has Alzheimers. We had a family portrait made into an oil and put in her room to help her remember us. The nurses always tell us how much she loves it and helps jog her memory. Thank you Brushvello Art!</p><div class="sep"></div><div class="name">Helen R</div><div class="place">Potomac, MD</div></div>
</section>

<h2 class="abs section-title" style="top:3620px">Why Us?</h2>

<div class="abs why" style="left:128px;top:3725px">
  <div class="badge"><svg width="48" height="48" viewBox="0 0 48 48" fill="none" stroke="#ef5a24" stroke-width="2.2"><rect x="8" y="8" width="14" height="10"/><rect x="8" y="22" width="14" height="18"/><rect x="26" y="8" width="14" height="18"/><rect x="26" y="30" width="14" height="10"/></svg></div>
  <h3>Your Idea Your Design</h3>
  <p>Each art piece is customized for you!<br>You choose your size, orientation and<br>art style. Makes a perfect gift!!!</p>
</div>
<div class="abs why" style="left:480px;top:3725px">
  <div class="badge"><svg width="52" height="48" viewBox="0 0 52 48" fill="none" stroke="#ef5a24" stroke-width="2.2"><rect x="6" y="12" width="26" height="20"/><path d="M32 18h8l6 7v7H32z"/><circle cx="14" cy="35" r="4"/><circle cx="38" cy="35" r="4"/><path d="M2 18h8M2 24h8"/></svg></div>
  <h3>Fast Shipping</h3>
  <p>Your artwork is printed and shipped in<br>the USA! We offer fast turnaround<br>with transit times typically 3-7 days.<br>Free tracking with each order!!</p>
</div>
<div class="abs why" style="left:835px;top:3725px">
  <div class="badge"><svg width="48" height="48" viewBox="0 0 48 48" fill="none" stroke="#ef5a24" stroke-width="2.2"><circle cx="24" cy="19" r="13"/><path d="M18 19l4 4 8-8M16 30l-5 13 6-3 3 6 4-13M32 30l5 13-6-3-3 6-4-13"/></svg></div>
  <h3>High Quality</h3>
  <p>We’ve put a lot of effort ensuring your<br>artwork is of the highest quality. Each<br>piece is printed on the highest quality,<br>gallery grade canvas. It is ready to<br>hang upon arrival!</p>
</div>

<footer class="abs footer">
  <div class="abs logo" style="left:133px;top:58px;font-size:28px"><span class="dot"></span>Brushvello Art</div>
  <div class="abs foot-contact">
    <svg width="26" height="20" viewBox="0 0 26 20" fill="none" stroke="#fff" stroke-width="1.6" style="margin-top:10px"><rect x="1" y="1" width="24" height="18"/><path d="M1 1l12 10 12-10"/></svg>
    <div>Email Us<br>info@brushvelloart.com</div>
  </div>
  <div class="abs follow">Follow us</div>
  <div class="abs socials"><span></span><span></span><span></span><span></span></div>
  <div class="abs foot-links">About Us<span>|</span>My Orders<span>|</span>Testimonials<span>|</span>Get Started<span>|</span>FAQs<span>|</span>Privacy Policy<span>|</span>Terms and Conditions</div>
  <div class="abs foot-rule"></div>
  <div class="abs copyright">Copyright © 2023 All Rights Reserved</div>
</footer>

</body>
</html>
```